Unique and original Business Card for Financial Services Business

I have moved premises and need to change the detail on my business card so thought now is a good time for a re-design. Looking for something professional and modern with colours to fit in with out logo. Like the idea of foil or embossing if that works but not a must have but I do want something that stands out and that I could not design myself.

Once business card is designed I will also be looking to get letterhead and flyers done but want the business card concept in place first.

The majority of designs I am receiving are generic and template based. I am looking for something unique and original. We have some great design elements in our logo, think outside the box and show me something that stands out from the crowd.

Target Market(s)

Business Professionals

Industry/Entity Type

Finance

Contact Information for Business Card

Name: Delphine Moore Phone 0438 297 614 Address PO Box 7816 Ashvale NSW 2411 Email info@tidewellmoneyservices.example.com.au website www.tidewellmoneyservices.example.com.au

Font styles to use
Other font styles liked:
• Ralway

Requirements
Should not have
• No black backgrounds please

```html
<!DOCTYPE html>
<html lang="en">
<head>
<meta charset="utf-8">
<title>Tidewell Money Services – Business Card</title>
<link rel="stylesheet" href="https://fonts.googleapis.com/css2?family=Open+Sans:wght@400;700&family=Raleway:wght@300;400&display=swap">
<style>
  :root {
    --page: #e9e4dc;
    --teal: #0a9a95;
    --teal-deep: #00485a;
    --teal-bright: #00a79f;
    --silver: #c8cfd2;
    --ink: #4a4f55;
    --ink-soft: #6b7076;
    --dark-band: #1d1f22;
    --wash-a: #e3f0f1;
    --wash-b: #f6fafa;
  }
  * { box-sizing: border-box; margin: 0; padding: 0; }
  html, body { width: 1200px; height: 985px; overflow: hidden; }
  body {
    background: var(--page);
    font-family: "Open Sans", Arial, sans-serif;
    display: flex; flex-direction: column; align-items: center; justify-content: center;
    gap: 50px;
  }
  .card {
    position: relative;
    width: 700px; height: 410px;
    border-radius: 30px;
    overflow: hidden;
    box-shadow: 0 12px 30px rgba(60, 50, 40, .18);
  }

  /* Front */
  .card-front {
    background: radial-gradient(ellipse at 55% 45%, var(--teal-bright) 0%, #007d80 45%, var(--teal-deep) 100%);
    display: flex; align-items: center; justify-content: center;
  }
  .front-brand {
    display: flex; align-items: center; gap: 22px;
    font-family: "Raleway", Arial, sans-serif; font-weight: 300;
    color: var(--silver);
  }
  .front-brand .brand-dot {
    width: 64px; height: 64px; border-radius: 50%;
    background: var(--silver);
  }
  .front-brand .brand-name { font-size: 46px; line-height: 1.1; letter-spacing: 1px; }
  .front-brand .brand-name span { display: block; font-size: 22px; letter-spacing: 9px; }

  /* Back */
  .card-back { background: #fff; }
  .back-decoration {
    position: absolute; left: 0; top: 90px;
    width: 400px; height: 320px;
    background: radial-gradient(ellipse at 50% 45%, var(--wash-a) 0%, var(--wash-b) 70%, #fff 100%);
  }
  .back-brand {
    position: absolute; right: 48px; top: 38px;
    display: flex; align-items: center; gap: 12px;
    font-family: "Raleway", Arial, sans-serif; font-weight: 400;
    color: var(--teal);
  }
  .back-brand .brand-dot { width: 34px; height: 34px; border-radius: 50%; background: var(--teal); }
  .back-brand .brand-name { font-size: 26px; line-height: 1.1; }
  .back-brand .brand-name span { display: block; font-size: 12.5px; letter-spacing: 5px; }
  .divider-top {
    position: absolute; left: 250px; right: 40px; top: 130px;
    height: 1.5px; background: var(--teal);
  }
  .address {
    position: absolute; right: 48px; top: 150px;
    text-align: right; color: var(--ink-soft); font-size: 14px; line-height: 1.5;
  }
  .person { position: absolute; left: 56px; top: 212px; }
  .person-name { color: var(--teal); font-weight: 700; font-size: 26px; letter-spacing: .5px; }
  .person-role { color: var(--ink-soft); font-size: 15px; margin-top: 2px; }
  .divider-bottom {
    position: absolute; left: 56px; width: 380px; top: 282px;
    height: 1.5px; background: var(--teal);
  }
  .contacts { position: absolute; left: 56px; top: 296px; list-style: none; }
  .contacts li {
    display: flex; align-items: center; gap: 9px;
    color: var(--ink); font-size: 13.5px; line-height: 1.65;
  }
  .contacts li.phone { font-weight: 700; }
  .contacts svg { width: 13px; height: 13px; fill: var(--teal); flex: none; }
  .edge-band {
    position: absolute; left: 0; right: 0; bottom: 0; height: 10px;
    display: flex;
  }
  .edge-band .band-teal { flex: 4; background: var(--teal); }
  .edge-band .band-dark { flex: 1; background: var(--dark-band); }
</style>
</head>
<body>

<section class="card card-front" aria-label="Card front">
  <div class="front-brand">
    <div class="brand-dot"></div>
    <div class="brand-name">TIDEWELL MONEY<span>Services</span></div>
  </div>
</section>

<section class="card card-back" aria-label="Card back">
  <div class="back-decoration" role="img" aria-label="Faint floral and hummingbird decoration in pale teal"></div>

  <div class="back-brand">
    <div class="brand-dot"></div>
    <div class="brand-name">TIDEWELL MONEY<span>Services</span></div>
  </div>

  <div class="divider-top"></div>

  <address class="address" style="font-style:normal">
    PO Box 7816<br>Ashvale, NSW 2411
  </address>

  <div class="person">
    <p class="person-name">DELPHINE MOORE</p>
    <p class="person-role">Founder &amp; CEO</p>
  </div>

  <div class="divider-bottom"></div>

  <ul class="contacts">
    <li class="phone">
      <svg viewBox="0 0 24 24" aria-hidden="true"><path d="M6.6 10.8a15 15 0 0 0 6.6 6.6l2.2-2.2a1 1 0 0 1 1-.25 11.4 11.4 0 0 0 3.6.57 1 1 0 0 1 1 1V20a1 1 0 0 1-1 1A17 17 0 0 1 3 4a1 1 0 0 1 1-1h3.5a1 1 0 0 1 1 1c0 1.25.2 2.45.57 3.57a1 1 0 0 1-.25 1z"/></svg>
      0438 297 614
    </li>
    <li>
      <svg viewBox="0 0 24 24" aria-hidden="true"><path d="M2 5h20v14H2z M2 5l10 8 10-8" stroke="#fff" stroke-width="1.5"/></svg>
      info@tidewellmoneyservices.example.com.au
    </li>
    <li>
      <svg viewBox="0 0 24 24" aria-hidden="true"><circle cx="12" cy="12" r="10"/></svg>
      www.tidewellmoneyservices.example.com.au
    </li>
  </ul>

  <div class="edge-band"><span class="band-teal"></span><span class="band-dark"></span></div>
</section>

</body>
</html>
```